Rivolex.com Trucking Company Website

Need a website designed (no content) for a trucking company, specializing in trucking of ocean containers (intermodal Trucking). Heavy emphasis on technology, using latest technology, providing unabated visibility and realtime information.
clean minimalist industrial website
example:
https://www.bramtiq.com/

Target Market(s)

Professional Business Consumer corporate and small business

Industry/Entity Type

Trucking Company

Number of Pages Required

5+ page

Requirements
Must have
• Industrial Design, simple informative, for a busy professional to view and get the necessary information with out the distractions.
• Blog Page
• Client Log-In on the front page
• Technology page - showing our intensive investments in technology
Nice to have
• If ANY images included, MUST be USA related. Example if include an image of a truck, ensure its a USA model. Do the research.
• included our business card for sample of Logo
• Doesnt not have to be the same color schemes.
Should not have
• moving images

```html
<!DOCTYPE html>
<html lang="en">
<head>
<meta charset="utf-8">
<title>Rivolex</title>
<link href="https://fonts.googleapis.com/css2?family=Lato:wght@300;400;700&display=swap" rel="stylesheet">
<style>
:root{
  --topbar:#232323;
  --footer:#1f1f1f;
  --blue:#1d5a9c;
  --blue-panel:rgba(30,95,165,.95);
  --accent:#f2c418;
  --heading:#1b5894;
  --body-text:#4a4a4a;
  --section-bg:#f1f1f1;
  --white:#fff;
}
*{margin:0;padding:0;box-sizing:border-box}
html,body{width:1200px;height:892px;overflow:hidden}
body{font-family:'Lato',sans-serif;position:relative;background:var(--section-bg);color:var(--body-text)}
.topbar{position:absolute;left:0;top:0;width:1200px;height:37px;background:var(--topbar);color:#e6e6e6;font-size:12px}
.topbar span{position:absolute;top:11px;display:flex;align-items:center;gap:5px;white-space:nowrap}
.topbar .sep{width:1px;height:16px;background:#666;top:11px}
.social{position:absolute;top:14px;width:9px;height:9px;background:#ddd}
.hero{position:absolute;left:0;top:37px;width:1200px;height:539px;
  background:linear-gradient(100deg,#6b5a4a 0%,#8a7a6a 20%,#3c3a3c 45%,#23283a 65%,#1b2232 100%)}
.hero-shade{position:absolute;inset:0;background:linear-gradient(180deg,rgba(40,40,60,.3),rgba(20,20,25,.55))}
.brand{position:absolute;left:27px;top:68px;display:flex;align-items:center;gap:10px;color:var(--white);font-weight:700;font-size:32px;line-height:1}
.brand-mark{width:18px;height:18px;background:var(--accent)}
.nav{position:absolute;top:77px;font-size:12.5px;font-weight:700;color:var(--white)}
.nav-line{position:absolute;left:27px;top:125px;width:1146px;height:1px;background:rgba(255,255,255,.4)}
.nav-active{position:absolute;left:741px;top:122px;width:35px;height:3px;background:var(--accent)}
.tag1{position:absolute;left:128px;top:232px;font-size:27px;font-weight:300;color:var(--white)}
.tag2{position:absolute;left:332px;top:270px;font-size:38px;font-weight:400;color:var(--white)}
.radios{position:absolute;left:172px;top:420px;font-size:12px;color:var(--white);display:flex;gap:10px}
.radios i{display:inline-block;width:9px;height:9px;border:1.5px solid #fff;border-radius:50%;margin-right:3px;vertical-align:-1px}
.radios i.on{background:radial-gradient(#fff 35%,transparent 40%)}
.search{position:absolute;left:172px;top:439px;width:856px;height:38px;background:var(--white);display:flex;font-size:12px;color:#444}
.search div{display:flex;align-items:center;gap:8px;padding-left:10px;border-right:1px solid #e3e3e3}
.ico{width:16px;height:14px;border-radius:2px}
.quote{position:absolute;left:172px;top:486px;width:145px;height:25px;background:var(--blue);color:var(--white);font-size:12px;font-weight:700;text-align:center;line-height:25px}
.welcome-art{position:absolute;left:0;top:580px;width:230px;height:240px;background:linear-gradient(160deg,#e3e3e3,#ececec);opacity:.8}
.rule{position:absolute;left:27px;top:628px;width:66px;height:2px;background:#444}
.welcome-title{position:absolute;left:27px;top:642px;font-size:24px;color:var(--heading);font-weight:400}
.welcome-text{position:absolute;left:27px;top:698px;width:725px;font-size:12.6px;line-height:20px;color:#444}
.partner{position:absolute;background:#d8d8d8;height:24px}
.panel{position:absolute;left:807px;top:508px;width:270px;height:334px;background:var(--blue-panel);color:var(--white);padding:16px 17px 0 18px}
.panel h2{font-size:20px;font-weight:400;margin-bottom:14px}
.panel label{display:block;font-size:12px;margin-bottom:4px}
.panel .field{background:#eef0f3;height:31px;margin-bottom:10px}
.panel .area{height:88px}
.panel .submit{width:85px;height:27px;background:#15202e;font-size:11.5px;font-weight:700;text-align:center;line-height:27px;letter-spacing:.5px}
.footer{position:absolute;left:0;top:842px;width:1200px;height:50px;background:var(--footer);color:#ddd;font-size:11.5px}
.footer span{position:absolute;top:18px}
.footer .links span{font-size:12.5px}
.totop{position:absolute;left:1145px;top:12px;width:29px;height:27px;background:#3a3a3a}
</style>
</head>
<body>
<header class="topbar">
  <span style="left:46px"><svg width="6" height="10"><rect x=".5" y=".5" width="5" height="9" rx="1" fill="none" stroke="#ddd"/></svg>Call us : &nbsp;555.318.2047</span>
  <span style="left:528px"><svg width="11" height="8"><rect width="11" height="8" fill="#ddd"/><path d="M0 0l5.5 4L11 0" stroke="#232323" fill="none"/></svg>Office : 420 Harbor Road Unit 3. Easton, NJ 0812</span>
  <span class="sep" style="left:822px"></span>
  <span style="left:839px"><svg width="11" height="8"><rect width="11" height="8" fill="#ddd"/><path d="M0 0l5.5 4L11 0" stroke="#232323" fill="none"/></svg>Email : &nbsp;dispatch@rivolex.com</span>
  <span class="sep" style="left:1037px"></span>
  <span style="left:1050px;font-size:13.5px;top:10px"><svg width="11" height="12"><circle cx="5.5" cy="3.5" r="3" fill="none" stroke="#ddd" stroke-width="1.4"/><path d="M1 12a4.5 4.5 0 0 1 9 0z" fill="#ddd"/></svg>Login</span>
  <span class="sep" style="left:1111px"></span>
  <i class="social" style="left:1124px"></i><i class="social" style="left:1142px"></i>
  <svg class="social" style="left:1160px;background:none" viewBox="0 0 9 9"><circle cx="1.5" cy="7.5" r="1.3" fill="#ddd"/><path d="M0 4a5 5 0 0 1 5 5M0 1a8 8 0 0 1 8 8" stroke="#ddd" stroke-width="1.4" fill="none"/></svg>
</header>

<section class="hero" role="img" aria-label="Photo of a truck driving on an open highway at sunset">
  <div class="hero-shade"></div>
</section>

<div class="brand"><span class="brand-mark"></span>Rivolex</div>
<nav>
  <span class="nav" style="left:741px">Home</span>
  <span class="nav" style="left:827px">Services</span>
  <span class="nav" style="left:927px">Technology</span>
  <span class="nav" style="left:1038px">Blog</span>
  <span class="nav" style="left:1112px">Contact Us</span>
  <div class="nav-line"></div><div class="nav-active"></div>
</nav>

<h1 class="tag1">WE MAKE EVERY MOVE APPEAR</h1>
<div class="tag2">EFFORTLESS</div>

<div class="radios"><span><i class="on"></i>Schedules &amp; Tariff</span><span><i></i>Truck Tracking</span></div>
<div class="search">
  <div style="width:204px"><span class="ico" style="background:#f29a2e"></span>Place of load</div>
  <div style="width:209px"><span class="ico" style="background:#e0463c"></span>Place of discharge</div>
  <div style="width:209px"><svg width="13" height="10"><path d="M0 1h2M4 1h9M0 5h2M4 5h9M0 9h2M4 9h9" stroke="#888"/></svg>Select Product Category &#8964;</div>
  <div style="width:189px"><span class="ico" style="background:#999;width:22px"></span>Shippers name &#8964;</div>
  <div style="width:45px;border:none;font-weight:700;font-size:13px;padding-left:12px">GO</div>
</div>
<div class="quote">Request a Freight Quote</div>

<div class="welcome-art" role="img" aria-label="Faint illustration of a warehouse with trucks and a forklift"></div>
<div class="rule"></div>
<h2 class="welcome-title">Welcome To Rivolex</h2>
<p class="welcome-text">Lorem ipsum dolor sit amet, consectetuer adipiscing elit, sed diam nonummy nibh euismod tincidunt ut laoreet dolore magna aliquam erat volutpat. Ut wisi enim ad minim veniam, quis nostrud exerci tation ullamcorper suscipit lobortis nisl ut aliquip ex ea commodo consequat. Duis autem vel eum iriure dolor in hendrerit in vulputate velit esse molestie consequat, vel illum dolore eu feugiat nulla facilisis at vero eros et accumsan.</p>

<div class="partner" style="left:1005px;top:666px;width:165px"></div>
<div class="partner" style="left:1060px;top:729px;width:110px;height:28px"></div>

<aside class="panel">
  <h2>Quick Contact</h2>
  <label>Name</label><div class="field"></div>
  <label>Email</label><div class="field"></div>
  <label>Message</label><div class="field area"></div>
  <div class="submit">SUBMIT</div>
</aside>

<footer class="footer">
  <span style="left:27px">Rivolex © 2017 All Rights Reserved</span>
  <div class="links">
    <span style="left:807px">Privacy</span>
    <span style="left:870px">Blog</span>
    <span style="left:915px">Technology</span>
    <span style="left:996px;color:#4a9ee0">Quick Contact</span>
  </div>
  <div class="totop"><svg width="29" height="27"><path d="M10 16l4.5-4.5L19 16" stroke="#aaa" stroke-width="1.6" fill="none"/></svg></div>
</footer>
</body>
</html>
```